Need 4 childhood cancer facts posters

Hello. I run a nonprofit in East Tennessee, USA that supports children with cancer and their families.

I need 4 poster designs with facts about childhood cancers. It should either have pictures of children with cancer or be focused around the whole idea of childhood cancer awareness. This project will require time and research. I will post links to facts as the project goes forward.

Questions can be emailed to tmarlowe@brightpathfund.org. AI format of our logo has been uploaded. I have images and links here http://www.brightpathfund.org/contest-pics.html

You can also view our website at www.brightpathfund.org

Some facts: http://dorvel.healthdata-example.org/archive/publications/childhood/

USE THESE FACTS: * Everyday, approximately 250 children will die from childhood cancer. *Childhood Cancers is the number 1 cause of death in children under age 15 in the US. *Less than 5% of the federal governments budget toward cancer research is dedicated to childhood cancers. *One in 330 children will be diagnosed with cancer by the time they are 20.

Poster will be 24 inches wide by 36 inches tall.

```html
<!DOCTYPE html>
<html lang="en">
<head>
<meta charset="utf-8">
<title>Childhood Cancer Awareness Poster</title>
<link rel="stylesheet" href="https://fonts.googleapis.com/css2?family=Ubuntu:wght@400;500;700&display=swap">
<style>
  :root {
    --ink: #4a4a4c;
    --sun: #fff23a;
    --paper: #ffffff;
  }
  html, body {
    margin: 0;
    padding: 0;
    width: 801px;
    height: 1200px;
    overflow: hidden;
    background: var(--paper);
  }
  .poster {
    position: relative;
    width: 801px;
    height: 1200px;
    overflow: hidden;
    background: var(--paper);
    font-family: "Ubuntu", sans-serif;
    color: var(--ink);
  }
  .headline-top {
    position: absolute;
    left: 118px;
    top: 168px;
    margin: 0;
    font-size: 114px;
    font-weight: 700;
    line-height: 1;
    letter-spacing: -1px;
    color: var(--ink);
  }
  .stat-band {
    position: absolute;
    left: 123px;
    top: 285px;
    width: 575px;
    height: 207px;
    background: var(--ink);
  }
  .stat-qualifier {
    position: absolute;
    left: 5px;
    top: 14px;
    margin: 0;
    font-size: 29px;
    font-weight: 700;
    color: var(--paper);
  }
  .stat-number {
    position: absolute;
    left: 266px;
    top: -22px;
    margin: 0;
    font-size: 182px;
    font-weight: 700;
    line-height: 1;
    letter-spacing: -3px;
    color: var(--sun);
  }
  .stat-subject {
    position: absolute;
    left: 270px;
    top: 139px;
    margin: 0;
    font-size: 63px;
    font-weight: 700;
    line-height: 1;
    color: var(--sun);
  }
  .headline-bottom {
    position: absolute;
    left: 118px;
    top: 490px;
    margin: 0;
    font-size: 126px;
    font-weight: 700;
    line-height: 1;
    letter-spacing: -1px;
    color: var(--ink);
  }
  .highlight {
    position: absolute;
    left: 113px;
    top: 608px;
    width: 570px;
    height: 60px;
    background: var(--sun);
  }
  .highlight-text {
    position: absolute;
    left: 12px;
    top: 4px;
    margin: 0;
    font-size: 44px;
    font-weight: 500;
    line-height: 1.1;
    color: var(--ink);
  }
  .foundation-mark {
    position: absolute;
    left: 0;
    top: 930px;
    width: 801px;
    display: flex;
    justify-content: center;
    align-items: center;
    gap: 14px;
  }
  .foundation-dot {
    width: 18px;
    height: 18px;
    border-radius: 50%;
    background: var(--sun);
  }
  .foundation-name {
    margin: 0;
    font-size: 22px;
    font-weight: 400;
    line-height: 1.35;
    letter-spacing: 2px;
    text-align: center;
    color: var(--ink);
  }
  .corner-stripes {
    position: absolute;
    left: 0;
    top: 0;
  }
</style>
</head>
<body>
  <main class="poster">
    <h1 class="headline-top">EVERYDAY</h1>

    <div class="stat-band">
      <p class="stat-qualifier">approximately</p>
      <p class="stat-number">250</p>
      <p class="stat-subject">CHILDREN</p>
    </div>

    <h2 class="headline-bottom">WILL DIE</h2>

    <div class="highlight">
      <p class="highlight-text">from childhood cancer.</p>
    </div>

    <div class="foundation-mark">
      <span class="foundation-dot"></span>
      <p class="foundation-name">BRIGHT PATH<br>CHILDHOOD CANCER<br>FOUNDATION</p>
    </div>

    <svg class="corner-stripes" width="801" height="1200" viewBox="0 0 801 1200" aria-hidden="true">
      <polygon points="801,967 801,1035 495,1200 398,1200" fill="var(--ink)"/>
      <polygon points="801,1035 801,1200 495,1200" fill="var(--sun)"/>
    </svg>
  </main>
</body>
</html>
```